3月15日にガールズバーをオープン致しました。
ビルの入り口に置いて使うA1立て看板の製作をお願いします。
A4など縮小サイズでもいただけると助かります。
白を基調とした夜でも目立つ感じにしたいです。

セット料金 40分2000円 tax&service 20%

チャージのみ1時間1500円 tax&service 15

クレジットチャージ 10%
飲み放題付き (焼酎 ウイスキー カクテルなど)
ビル3階 席数17席  団体客歓迎

若いギャル系の女の子の写真を大きく入れて頂きたいのですが素材が無く
困ってます。素材をお持ちかたにお願いしたいと思ってます。

現在の看板を添付致しました。ご参考までに。
文章は記載しないでも大丈夫です。

店舗名 Sunflower(サンフラワー)です。

よろしくお願いします。
資料を再添付致しました。よろしくお願いします。
依頼金額を25000円に変更して、延長しました。
提案下さった皆様ありがとうございます。
もう少し提案を見させていただけたらと思います。

具体的なイメージをデザベース様の過去の事例で近いものを添付致しました。
よろしくお願いします。

最初に思い描いてたイメージより良かったです
女の子と背景のピンクもかわいいくて満足です。

ありがとうございました!

提案くださった皆様ありがとうございます!
修正をしてくださった皆様も早急な対応に感謝致します。

ありがとうございました!

```html
<!DOCTYPE html>
<html lang="ja">
<head>
<meta charset="utf-8">
<title>Sunflower Girls Bar</title>
<link href="https://fonts.googleapis.com/css2?family=Playfair+Display:ital,wght@0,700;0,900;1,700&family=Noto+Serif+JP:wght@700;900&family=M+PLUS+Rounded+1c:wght@700;800&display=swap" rel="stylesheet">
<style>
  :root{
    --pink:#ec5a8e;
    --pink-deep:#e0407a;
    --pink-soft:#fbe3ec;
    --gold:#b6925a;
    --gold-light:#d8bd8c;
    --band:#cdb48a;
    --ink:#2b211b;
    --white:#ffffff;
  }
  *{margin:0;padding:0;box-sizing:border-box}
  html,body{width:848px;height:1200px;overflow:hidden;background:var(--white)}
  .poster{position:relative;width:848px;height:1200px;overflow:hidden;
    background:linear-gradient(180deg,#fff 0%,#fdf2f6 45%,#fbe6ee 88%);
    font-family:"M PLUS Rounded 1c",sans-serif}
  .hero-photo{position:absolute;left:300px;top:110px;width:548px;height:760px;
    background:radial-gradient(ellipse at 55% 40%,#e9cbbd 0%,#d9b09c 30%,#f3e4e4 62%,rgba(253,242,246,0) 80%)}
  .title{position:absolute;left:28px;top:26px;font-family:"Playfair Display",serif;font-weight:900;
    font-size:70px;color:var(--gold);display:flex;align-items:center;gap:10px;letter-spacing:1px}
  .title svg{width:38px;height:34px}
  .shop-mark{position:absolute;right:34px;top:24px;text-align:center;color:var(--pink)}
  .shop-mark .en{font-family:"Playfair Display",serif;font-weight:700;font-size:40px;line-height:1}
  .shop-mark .ja{font-size:16px;font-weight:700;margin-top:2px}
  .price-head{position:absolute;left:28px;font-family:"Noto Serif JP",serif;font-weight:900;font-size:30px;color:var(--pink-deep)}
  .price-head .free{font-family:"Playfair Display",serif;font-style:italic;font-weight:700;margin-left:18px;font-size:32px}
  .price-row{position:absolute;left:18px;display:flex;align-items:center;gap:4px}
  .heart{position:relative;width:96px;height:86px}
  .heart svg{position:absolute;inset:0;width:100%;height:100%}
  .heart span{position:absolute;inset:0;display:flex;flex-direction:column;align-items:center;justify-content:center;
    color:var(--white);font-family:"Playfair Display",serif;font-style:italic;font-size:24px;line-height:1;padding-bottom:8px}
  .heart span small{font-size:17px}
  .amount{font-family:"Noto Serif JP",serif;font-weight:900;font-size:78px;color:var(--pink-deep);letter-spacing:-1px;line-height:1}
  .amount em{font-style:normal;font-size:46px}
  .tax{position:absolute;left:124px;font-family:"Playfair Display",serif;font-style:italic;font-size:24px;color:var(--pink-deep)}
  .credit{position:absolute;left:28px;top:582px;font-family:"Noto Serif JP",serif;font-weight:900;font-size:26px;color:var(--pink-deep)}
  .drinks{position:absolute;left:40px;top:626px;font-family:"Noto Serif JP",serif;font-weight:900;font-size:110px;color:var(--gold);line-height:1.1;letter-spacing:2px}
  .drinks-list{position:absolute;left:44px;top:760px;font-family:"Noto Serif JP",serif;font-weight:900;font-size:34px;color:var(--pink-deep)}
  .catch{position:absolute;left:570px;top:745px;transform:rotate(-16deg);font-family:"Noto Serif JP",serif;font-weight:900;
    font-size:30px;color:var(--pink-deep);line-height:1.35;text-align:center}
  .seats{position:absolute;left:44px;top:850px;font-family:"Noto Serif JP",serif;font-weight:900;font-size:52px;color:var(--gold)}
  .group{position:absolute;left:30px;top:925px;display:flex;align-items:center;background:var(--pink);padding:8px 10px 8px 20px;
    font-family:"Noto Serif JP",serif;font-weight:900;font-size:58px;color:var(--white);border-radius:4px}
  .group b{background:var(--white);color:var(--pink-deep);padding:0 10px;margin-left:10px;border-radius:6px}
  .floor{position:absolute;left:592px;top:898px;width:256px;height:126px}
  .floor svg{position:absolute;inset:0;width:100%;height:100%}
  .floor p{position:absolute;left:36px;top:10px;color:var(--white);font-family:"Noto Serif JP",serif;font-weight:900;font-size:32px;white-space:nowrap}
  .floor p strong{font-size:84px;vertical-align:-8px}
  .footer{position:absolute;left:0;bottom:0;width:848px;height:160px;background:linear-gradient(180deg,var(--gold-light),var(--band))}
  .footer .shop{position:absolute;left:64px;top:18px;color:var(--ink);text-align:center}
  .footer .shop .en{font-family:"Playfair Display",serif;font-weight:900;font-size:84px;line-height:1}
  .footer .shop .ja{font-family:"Noto Serif JP",serif;font-weight:700;font-size:24px;text-align:left;margin-top:2px}
  .hours{position:absolute;right:40px;top:34px;display:flex;flex-direction:column;gap:12px}
  .hours div{display:flex;align-items:center;gap:14px;font-family:"Playfair Display",serif;font-weight:700;font-size:40px;color:var(--ink)}
  .hours span{background:var(--ink);color:var(--white);font-size:24px;padding:2px 10px;width:112px;text-align:center;letter-spacing:2px}
</style>
</head>
<body>
<div class="poster">
  <div class="hero-photo" role="img" aria-label="長い茶髪の若い女性が白いニットで微笑むポートレート写真"></div>

  <div class="title">
    <svg viewBox="0 0 32 28"><path d="M16 27 C4 18 0 12 0 7 A7 7 0 0 1 16 4 A7 7 0 0 1 32 7 C32 12 28 18 16 27Z" fill="#b6925a"/></svg>
    Girls Bar
  </div>
  <div class="shop-mark"><div class="en">Sunflower</div><div class="ja">サンフラワー</div></div>

  <div class="price-head" style="top:150px">セット料金<span class="free">Free Drink</span></div>
  <div class="price-row" style="top:196px">
    <div class="heart"><svg viewBox="0 0 32 28"><path d="M16 27 C4 18 0 12 0 7 A7 7 0 0 1 16 4 A7 7 0 0 1 32 7 C32 12 28 18 16 27Z" fill="#ec5a8e"/></svg><span>40<small>min</small></span></div>
    <div class="amount">2,000<em>円</em></div>
  </div>
  <div class="tax" style="top:288px">tax &amp; service 20%</div>

  <div class="price-head" style="top:340px">チャージのみ</div>
  <div class="price-row" style="top:388px">
    <div class="heart"><svg viewBox="0 0 32 28"><path d="M16 27 C4 18 0 12 0 7 A7 7 0 0 1 16 4 A7 7 0 0 1 32 7 C32 12 28 18 16 27Z" fill="#ec5a8e"/></svg><span>60<small>min</small></span></div>
    <div class="amount">1,500<em>円</em></div>
  </div>
  <div class="tax" style="top:480px">tax &amp; service 15%</div>
  <div class="credit">クレジットチャージ 10%</div>

  <div class="drinks">飲み放題!!</div>
  <div class="drinks-list">焼酎 ウイスキー カクテルetc...</div>
  <div class="catch">可愛い子たちと<br>気軽に遊べる!</div>

  <div class="seats">席数17席</div>
  <div class="group">団体客様<b>歓迎</b></div>
  <div class="floor">
    <svg viewBox="0 0 256 126" preserveAspectRatio="none"><polygon points="24,0 256,0 256,126 0,126" fill="#ec5a8e"/></svg>
    <p>当ビル<strong>3</strong>階</p>
  </div>

  <div class="footer">
    <div class="shop"><div class="en">Sunflower</div><div class="ja">サンフラワー</div></div>
    <div class="hours">
      <div><span>OPEN</span>20:00</div>
      <div><span>CLOSE</span>5:00</div>
    </div>
  </div>
</div>
</body>
</html>
```